Accident Law Firm Billboard Bold Easy to See Car Accidents

We need a billboard design that can catch attention in a very crowed Car Accident lawyer market. We wish to feature the phone number (407) 555-0148 as the focus of the Bill Board. We are trying to get the phone number recognized and remembered by drivers. The law firm name is not as crucial to remember.
Basically, It's CAR ACCIDENT? Then (407) 555-0148. We are not married to any specific color scheme but it has to POP and catch attention.
So the Crucial elements are as follows:
1. Phone number (407) 555-0148
2. Words CAR ACCIDENT?
3. Firm Logo in lower portion or where appropriate. Firm Logo to be provided
4. We may want to try a Day Glow orange color, with White and Black added. An example of the color scheme shall be provided.
5. Possible "Catch Phrase" to be used, "It's Time Call 9"
Target Market(s)
Orlando Florida Car Accident victims
Industry/Entity Type
Law Firm
Requirements
Must have
- Easy to see phone number (407) 555-0148
- Catch attention
Nice to have
- I would like to have the sign visible in bright sunlight and it not too hard to immediately know what phone number is for
Should not have
- too many words
- No bold enough
- confusing fonts
- Unclear fonts

```html
<!DOCTYPE html>
<html lang="en">
<head>
<meta charset="UTF-8">
<title>Car Accident Billboard</title>
<link rel="stylesheet" href="https://fonts.googleapis.com/css2?family=Archivo:wdth,wght@125,900&family=Oswald:wght@600;700&family=Montserrat:wght@600;800&display=swap">
<style>
  :root {
    --page-bg: #ffffff;
    --board-bg: #ffffff;
    --ink: #111111;
    --signal-red: #e0402b;
    --signal-red-deep: #c42a21;
    --tagline-red: #bf1a1f;
    --rule-red: #c8231f;
    --number-white: #f7f7f5;
  }
  * { margin: 0; padding: 0; box-sizing: border-box; }
  html, body {
    width: 1200px;
    height: 1200px;
    overflow: hidden;
    background: var(--page-bg);
  }
  .canvas {
    position: relative;
    width: 1200px;
    height: 1200px;
  }
  .billboard {
    position: absolute;
    left: 50px;
    top: 350px;
    width: 1100px;
    height: 500px;
    background: var(--board-bg);
    box-shadow: 0 2px 6px rgba(0,0,0,0.12);
  }
  .headline {
    position: absolute;
    top: 18px;
    left: 0;
    width: 100%;
    text-align: center;
    font-family: "Archivo", "Arial Black", sans-serif;
    font-stretch: 125%;
    font-weight: 900;
    font-size: 98px;
    line-height: 1;
    letter-spacing: -3px;
    color: var(--ink);
  }
  .phone-band {
    position: absolute;
    top: 133px;
    left: 0;
    width: 100%;
    height: 200px;
    background: linear-gradient(180deg, var(--signal-red) 0%, var(--signal-red-deep) 100%);
    display: flex;
    align-items: center;
    justify-content: center;
    gap: 14px;
    color: var(--number-white);
    font-family: "Oswald", "Arial Narrow", sans-serif;
    font-weight: 700;
  }
  .phone-area {
    font-size: 122px;
    font-weight: 600;
    line-height: 1;
    margin-top: 24px;
  }
  .phone-local {
    font-size: 192px;
    line-height: 1;
    letter-spacing: 2px;
  }
  .tagline {
    position: absolute;
    top: 350px;
    left: 0;
    width: 100%;
    text-align: center;
    font-family: "Montserrat", Arial, sans-serif;
    font-weight: 600;
    font-size: 62px;
    line-height: 1;
    letter-spacing: 0.32em;
    color: var(--tagline-red);
  }
  .signature {
    position: absolute;
    top: 430px;
    left: 0;
    width: 100%;
    height: 70px;
    display: flex;
    align-items: center;
    gap: 22px;
  }
  .signature-rule {
    flex: 1;
    height: 3px;
    background: var(--rule-red);
  }
  .firm-name {
    font-family: "Montserrat", Arial, sans-serif;
    font-weight: 800;
    font-size: 26px;
    letter-spacing: 0.12em;
    color: var(--ink);
    white-space: nowrap;
  }
</style>
</head>
<body>
  <div class="canvas">
    <section class="billboard">
      <h1 class="headline">CAR ACCIDENT?</h1>
      <div class="phone-band">
        <span class="phone-area">(407)</span>
        <span class="phone-local">555-0148</span>
      </div>
      <p class="tagline">It's Time Call 9</p>
      <div class="signature">
        <span class="signature-rule"></span>
        <span class="firm-name">MARVELLO LAW FIRM P.C.</span>
        <span class="signature-rule"></span>
      </div>
    </section>
  </div>
</body>
</html>
```